Design Business Cards and a logo for Bluegum Safeguard an insurance advice business

We run an existing financial planning company called Larkhill Planned, we have recently started a new business called Bluegum Safeguard which is focused solely at providing life insurance advice to clients.

Attached is our existing business cards for current company.

The only difference for contact details will be that the email address will be dennis@[login to view URL], the phone number will be (07) 3948 2650, the URL is also now bluegumsafeguard.com.au.

I would like a completely different design, however I do need the qualifications, and disclaimer bit included.

On the back of the card it would be good if it listed the following types of insurance advice

1. Life insurance and TPD
2. Trauma cover
3. Income protection
4. Key man and loan cover
5. Buy/sell insurance funded agreements

More work to follow for the right applicant

```html
<!DOCTYPE html>
<html lang="en">
<head>
<meta charset="utf-8">
<title>Bluegum Safeguard – Business Card</title>
<link rel="stylesheet" href="https://fonts.googleapis.com/css2?family=Arimo:wght@400;700&family=Lora:wght@400&family=Roboto:wght@400&display=swap">
<style>
  :root {
    --page-bg: #e8e5e0;
    --card-dark: #222222;
    --card-darker: #181818;
    --band-black: #0b0b0b;
    --name-box: #121212;
    --gold-light: #f6d36a;
    --gold: #d6a21e;
    --gold-deep: #8a5e07;
    --brand-gold: #d9a82a;
    --mark-silver: #b8b8b8;
    --text-white: #f4f4f4;
  }
  * { box-sizing: border-box; margin: 0; padding: 0; }
  html, body {
    width: 1200px;
    height: 880px;
    overflow: hidden;
    background: var(--page-bg);
  }
  .card {
    position: absolute;
    left: 80px;
    top: 120px;
    width: 1040px;
    height: 640px;
    border-radius: 22px;
    overflow: hidden;
    box-shadow: 0 10px 30px rgba(0,0,0,0.25);
  }
  .card-texture {
    position: absolute;
    inset: 0;
    background: radial-gradient(ellipse at 40% 30%, var(--card-dark), var(--card-darker));
  }
  .brand-name {
    position: absolute;
    top: 52px;
    left: 230px;
    font-family: "Roboto", sans-serif;
    font-weight: 400;
    font-size: 58px;
    letter-spacing: 1px;
    color: var(--brand-gold);
    white-space: nowrap;
  }
  .services-band {
    position: absolute;
    top: 150px;
    left: 62px;
    width: 880px;
    height: 300px;
    background: var(--band-black);
  }
  .gold-bar {
    position: absolute;
    top: 140px;
    width: 24px;
    height: 330px;
    border-radius: 12px;
    background: linear-gradient(90deg, var(--gold-deep), var(--gold-light) 45%, var(--gold) 70%, var(--gold-deep));
  }
  .gold-bar--left { left: 44px; }
  .gold-bar--right { left: 960px; }
  .services-list {
    position: absolute;
    top: 168px;
    left: 110px;
    list-style: none;
    font-family: "Arimo", sans-serif;
    font-size: 24px;
    color: var(--text-white);
    letter-spacing: 0.5px;
  }
  .services-list li { height: 52px; line-height: 52px; }
  .brand-mark {
    position: absolute;
    top: 196px;
    left: 700px;
    width: 232px;
    height: 232px;
    border-radius: 50%;
    background: var(--mark-silver);
  }
  .contact-box {
    position: absolute;
    top: 472px;
    left: 250px;
    width: 630px;
    height: 136px;
    border-radius: 12px;
    background: var(--name-box);
    text-align: center;
    color: var(--text-white);
    padding-top: 14px;
  }
  .person-name {
    font-family: "Arimo", sans-serif;
    font-weight: 700;
    font-size: 30px;
    letter-spacing: 0.5px;
  }
  .person-role {
    font-family: "Lora", serif;
    font-size: 28px;
    margin-top: 2px;
  }
  .person-quals {
    font-family: "Arimo", sans-serif;
    font-weight: 700;
    font-size: 17px;
    margin-top: 6px;
  }
</style>
</head>
<body>
  <div class="card">
    <div class="card-texture" role="img" aria-label="Dark charcoal damask pattern texture"></div>

    <div class="brand-name">BLUEGUM SAFEGUARD</div>

    <div class="services-band"></div>
    <div class="gold-bar gold-bar--left"></div>
    <div class="gold-bar gold-bar--right"></div>

    <ul class="services-list">
      <li>LIFE INSURANCE AND TPD</li>
      <li>INCOME PROTECTION</li>
      <li>TRAUMA COVER</li>
      <li>KEY MAN AND LOAN COVER</li>
      <li>BUY/SELL INSURANCE FUNDED AGREEMENTS</li>
    </ul>

    <div class="brand-mark"></div>

    <div class="contact-box">
      <div class="person-name">DENNIS HARTWELL</div>
      <div class="person-role">Private Client Financial Planner</div>
      <div class="person-quals">MASTERS OF FINANCIAL PLANNING ADV DIP FIN PLAN C.DEC</div>
    </div>
  </div>
</body>
</html>
```